Marrowfell Website Concept

We would like a one page website. Please refer to the attached files for more information.

Please reference file attachment version 1.1.

```html
<!DOCTYPE html>
<html lang="en">
<head>
<meta charset="utf-8">
<title>Marrowfell — Security Firm</title>
<link href="https://fonts.googleapis.com/css2?family=Source+Sans+3:wght@400;600&display=swap" rel="stylesheet">
<style>
:root{
  --navy:#1c3a5c;
  --accent:#2aa6dd;
  --band-blue:#183f5f;
  --text:#444a52;
  --muted:#777d85;
  --black:#000;
  --field:#3a3a3a;
  --white:#fff;
}
*{margin:0;padding:0;box-sizing:border-box}
html,body{width:671px;height:1200px;overflow:hidden}
body{font-family:"Source Sans 3",sans-serif;color:var(--text);background:var(--white);position:relative}
.abs{position:absolute}
/* header */
.site-header{top:0;left:0;width:671px;height:44px;background:var(--white)}
.brand{left:168px;top:10px;font-size:17px;font-weight:600;color:var(--navy);letter-spacing:.5px;display:flex;align-items:center;gap:6px}
.brand-dot{width:14px;height:14px;border-radius:50%;background:var(--navy)}
.main-nav{top:28px;left:350px;font-size:6px;display:flex;gap:12px;color:var(--navy)}
.main-nav .active{color:var(--accent)}
/* hero */
.hero{top:44px;left:0;width:671px;height:198px;background:radial-gradient(ellipse at 50% 60%,#5c7591,#2d4a6b 70%,#22395a)}
.hero-title{top:78px;width:671px;text-align:center;color:var(--white);font-size:12px;letter-spacing:.3px}
.hero-sub{top:97px;left:245px;width:181px;text-align:center;color:var(--white);font-size:5.5px;line-height:1.4}
.btn{display:flex;align-items:center;justify-content:center;font-size:5.5px;border-radius:9px}
.hero-btn{top:131px;left:314px;width:60px;height:17px;background:var(--navy);color:var(--white)}
/* services */
.section-title{width:671px;text-align:center;font-size:10px;color:var(--navy);letter-spacing:.3px}
.services-title{top:271px}
.laptop{top:304px;left:168px;width:138px;height:78px;background:linear-gradient(#eef1f4,#c9d2db);border:4px solid #2a2a2a;border-bottom-width:6px;border-radius:3px}
.service{width:80px;display:flex;gap:6px}
.service-icon{width:10px;height:10px;flex:none;margin-top:1px}
.service h3{font-size:5.5px;font-weight:400;color:var(--navy);line-height:1.2}
.service p{font-size:4.5px;color:var(--muted);line-height:1.35;margin-top:3px}
/* band */
.band{top:420px;left:0;width:671px;height:144px;background:radial-gradient(ellipse at 40% 50%,#4a4a4a,#1d1d1d 60%,#111)}
.band-text{top:484px;width:671px;text-align:center;color:var(--white);font-size:8.5px;line-height:1.25}
.band-text em{font-style:normal;color:var(--accent)}
.band-btn{top:510px;left:314px;width:44px;height:15px;border:1px solid #888;color:#ccc;font-size:5px}
/* project */
.project{top:564px;left:0;width:671px;height:186px;background:var(--band-blue)}
.project-title{top:600px;left:168px;font-size:12px;color:var(--white);font-weight:400}
.project-lead{top:625px;left:168px;width:150px;font-size:6px;color:#a9c8e2;line-height:1.35}
.project-h{top:653px;left:168px;font-size:5.5px;color:var(--white)}
.project-p{top:666px;left:168px;width:170px;font-size:4.5px;color:#a9c8e2;line-height:1.4}
.project-link{top:701px;left:168px;font-size:5px;color:#cfe0ee;display:flex;gap:4px;align-items:center}
.tablet{top:606px;left:366px;width:128px;height:102px;background:linear-gradient(135deg,#2d3a46,#10161c);border-radius:6px;transform:skewY(-3deg)}
/* cta */
.cta-title{top:784px}
.cta-btn{top:806px;left:310px;width:48px;height:16px;border:1px solid var(--navy);color:var(--navy)}
.social{top:844px;width:24px;height:24px;border-radius:50%;background:var(--accent)}
/* footer */
.site-footer{top:900px;left:0;width:671px;height:300px;background:var(--black)}
.footer-title{top:936px;left:167px;font-size:10px;color:var(--white)}
.footer-lead{top:951px;left:167px;font-size:4.5px;color:#aaa}
.form-label{top:963px;left:167px;font-size:6px;color:var(--white)}
.field{height:14px;background:var(--field);font-size:4.5px;color:#999;padding:4px 5px}
.send{top:1136px;left:245px;width:62px;height:15px;display:flex}
.send span{flex:1;background:#333;color:#ddd;font-size:4.5px;display:flex;align-items:center;justify-content:center}
.send i{width:17px;background:#2b56a4;display:flex;align-items:center;justify-content:center}
.footer-links{top:1166px;left:167px;font-size:4.5px;color:#bbb}
.copyright{top:1175px;left:167px;font-size:4.5px;color:#888}
.footer-brand{top:948px;left:361px;font-size:12px;font-weight:600;color:#ccc;display:flex;gap:5px;align-items:center}
.footer-brand .brand-dot{background:#888;width:11px;height:11px}
.map{top:978px;left:361px;width:133px;height:61px;background:#d9d9d9}
.addr-h{top:1051px;left:361px;font-size:6px;color:var(--white)}
.addr{top:1062px;left:361px;font-size:4.5px;color:#aaa;line-height:1.5}
.contact-line{left:361px;font-size:4.5px;color:#aaa;display:flex;gap:6px;align-items:center}
</style>
</head>
<body>
<header class="site-header abs">
  <div class="brand abs"><span class="brand-dot"></span>Marrowfell</div>
  <nav class="main-nav abs"><span class="active">HOME</span><span>ABOUT</span><span>BLOG</span><span>PORTFOLIO</span><span>CONTACT</span></nav>
</header>

<section class="hero abs" role="img" aria-label="Close-up photo of a keyboard with a red padlock key"></section>
<h1 class="hero-title abs" style="font-weight:400">SECURITY FIRM SPECIALIZING</h1>
<p class="hero-sub abs">IN THE PROTECTION OF FINANCIAL SERVICES PROFESSIONALS, EXECUTIVES AND THEIR FAMILIES</p>
<div class="hero-btn btn abs">VIEW PORTFOLIO</div>

<h2 class="section-title services-title abs" style="font-weight:400">PROFESSIONAL SERVICES</h2>
<div class="laptop abs" role="img" aria-label="Laptop showing the website"></div>
<div class="service abs" style="top:304px;left:332px">
  <svg class="service-icon" viewBox="0 0 10 10"><rect x="2" y="4.5" width="6" height="5" fill="#555"/><path d="M3.3 4.5V3a1.7 1.7 0 0 1 3.4 0v1.5" fill="none" stroke="#555" stroke-width="1"/></svg>
  <div><h3>Threat<br>Assessment</h3><p>Lorem ipsum is simply dummy text of the printing and typesetting industry. Lorem ipsum has been.</p></div>
</div>
<div class="service abs" style="top:304px;left:422px">
  <svg class="service-icon" viewBox="0 0 10 10"><rect x="2" y="1" width="6" height="8" fill="none" stroke="#555"/><path d="M3.5 3.5h3M3.5 5h3M3.5 6.5h3" stroke="#555" stroke-width=".7"/></svg>
  <div><h3>Threat Avoidance<br>Plan &amp; Dossier Creation</h3><p>Lorem ipsum is simply dummy text of the printing and typesetting industry.</p></div>
</div>
<div class="service abs" style="top:354px;left:332px">
  <svg class="service-icon" viewBox="0 0 10 10"><path d="M5 1l4 1.5v3C9 8 5 9.5 5 9.5S1 8 1 5.5v-3z" fill="#555"/></svg>
  <div><h3>Elite Executive<br>Protection</h3><p>Lorem ipsum is simply dummy text of the printing and typesetting industry.</p></div>
</div>
<div class="service abs" style="top:354px;left:422px">
  <svg class="service-icon" viewBox="0 0 10 10"><rect x="1" y="3" width="8" height="5" fill="none" stroke="#555"/><path d="M1 5h8" stroke="#555" stroke-width=".7"/></svg>
  <div><h3>Threat Avoidance<br>Plan &amp; Dossier Maintenance</h3><p>Lorem ipsum is simply dummy text of the printing and typesetting.</p></div>
</div>

<section class="band abs" role="img" aria-label="Dark digital world map with hexagons and numbers"></section>
<p class="band-text abs">Lorem Ipsum is <em>simply dummy text</em> of the printing<br>and typesetting industry</p>
<div class="band-btn btn abs">LEARN MORE</div>

<section class="project abs"></section>
<h2 class="project-title abs">Latest Project</h2>
<p class="project-lead abs">Lorem Ipsum is simply dummy text of the printing and typesetting industry</p>
<h3 class="project-h abs" style="font-weight:400">DEVELOPING A FRAMEWORK</h3>
<p class="project-p abs">Lorem Ipsum is simply dummy text of the printing and typesetting industry. Lorem Ipsum has been the industry's standard dummy text ever since the 1500s, when an unknown printer took a galley of type and scrambled it to make a type specimen book.</p>
<div class="project-link abs">VIEW DETAIL <svg width="8" height="4" viewBox="0 0 8 4"><path d="M0 2h7M5 .5L7 2 5 3.5" fill="none" stroke="#cfe0ee" stroke-width=".6"/></svg></div>
<div class="tablet abs" role="img" aria-label="Tablet showing a security app"></div>

<h2 class="section-title cta-title abs" style="font-weight:400">READY TO TALK ABOUT OUR NEXT PROJECT</h2>
<div class="cta-btn btn abs">CONTACT US</div>
<div class="social abs" style="left:288px" aria-label="Social profile 1"></div>
<div class="social abs" style="left:323px" aria-label="Social profile 2"></div>
<div class="social abs" style="left:358px" aria-label="Social profile 3"></div>

<footer class="site-footer abs"></footer>
<h2 class="footer-title abs" style="font-weight:400">Get to know us completely just</h2>
<p class="footer-lead abs">Lorem ipsum is simply dummy text of the printing and typesetting industry</p>
<p class="form-label abs">Contact Form</p>
<div class="field abs" style="top:978px;left:167px;width:140px">First Name</div>
<div class="field abs" style="top:995px;left:167px;width:140px">Last Name</div>
<div class="field abs" style="top:1012px;left:167px;width:45px">Home Phone</div>
<div class="field abs" style="top:1012px;left:214px;width:45px">Work Phone</div>
<div class="field abs" style="top:1012px;left:261px;width:46px">Cell Phone</div>
<div class="field abs" style="top:1028px;left:167px;width:140px">Email Address</div>
<div class="field abs" style="top:1045px;left:167px;width:140px">Address</div>
<div class="field abs" style="top:1062px;left:167px;width:45px">City</div>
<div class="field abs" style="top:1062px;left:214px;width:45px">State</div>
<div class="field abs" style="top:1062px;left:261px;width:46px">Zipcode</div>
<div class="field abs" style="top:1079px;left:167px;width:140px;height:45px">Message</div>
<div class="send abs"><span>SEND MESSAGE</span><i><svg width="7" height="6" viewBox="0 0 7 6"><path d="M.5 3l2 2L6.5.5" fill="none" stroke="#fff" stroke-width="1"/></svg></i></div>
<p class="footer-links abs">Home &nbsp;|&nbsp; About Us &nbsp;|&nbsp; Award Winning &nbsp;|&nbsp; Content &nbsp;|&nbsp; Career &nbsp;|&nbsp; Contact Us</p>
<p class="copyright abs">Copyright © 2014 MARROWFELL &nbsp;|&nbsp; PRIVACY POLICY</p>

<div class="footer-brand abs"><span class="brand-dot"></span>Marrowfell</div>
<div class="map abs" role="img" aria-label="Street map with location pin"></div>
<p class="addr-h abs">Address</p>
<p class="addr abs">27 Harlow Lane, Brindmoor,<br>CA 90417</p>
<div class="contact-line abs" style="top:1083px"><svg width="5" height="5" viewBox="0 0 5 5"><path d="M1 .5l1 1-.5.8a3 3 0 0 0 1.2 1.2l.8-.5 1 1-.7.7C2.5 4.7.3 2.5.3 1.2z" fill="#aaa"/></svg>+1 555 014 2290</div>
<div class="contact-line abs" style="top:1091px"><svg width="5" height="5" viewBox="0 0 5 5"><rect x=".3" y="1" width="4.4" height="3" fill="none" stroke="#aaa" stroke-width=".5"/><path d="M.3 1l2.2 1.6L4.7 1" fill="none" stroke="#aaa" stroke-width=".5"/></svg>hello@marrowfell.test</div>
<div class="contact-line abs" style="top:1099px"><svg width="5" height="5" viewBox="0 0 5 5"><circle cx="2.5" cy="2.5" r="2" fill="none" stroke="#aaa" stroke-width=".5"/></svg>www.marrowfell.test</div>
</body>
</html>
```